2 sided Handyman Postcard Design with coupon on the back

Company name is "Miles ReadyFix" Looking for a postcard that's also a business card. Showing Miles ReadyFix, 4172 Tamber Glen Rd NE, Washington C.H., Ohio 43160, 740-318-2964, dkweller@mailbrook.net coupon- $25 off any job over $100, $50 off any job over $250, $75 off any job over $500, $100 off any job over $750, qualifications, experience 25 years. No job is to small. Handyman service. home repair. Free estimates. Examples, Flooring, Cabinets, Decks, Odd Jobs, Carpentry, Painting, Drywall repair, Ceramic tile, Screen repair, fence repair, Pressure wash, Hang a Picture, wood rot repair, Plumbing, Electrical, Small Jobs, Install ceiling fan, replace garbage disposal, toilet repair, install new lighting, Install safety grab bars, caulk tub or Kitchen, Hang Blinds/rods, Replace a switch/outlet, Replace/adjust doors and locksets, replace faucets/sinks/vanity tops, And much more. Have a signature look, I wear a ranger drifton hat on the job, full beard, and glasses. Am looking for a caricature of that with tools as main logo which should be shown on front and the back. One year warranty, Bonded, Insured. Cash or checks

```html
<!DOCTYPE html>
<html lang="en">
<head>
<meta charset="utf-8">
<title>Miles ReadyFix – Handyman Postcard</title>
<link href="https://fonts.googleapis.com/css2?family=Delius&display=swap" rel="stylesheet">
<style>
  :root {
    --ink: #141414;
    --blue: #1f3b9f;
    --navy: #0c2a5f;
    --white: #ffffff;
    --bg-light: #e9e8e8;
    --bg-mid: #d6d0cc;
    --bg-warm: #bfa897;
    --figure-a: #d9cdb8;
    --figure-b: #9fb2cf;
  }
  html, body {
    margin: 0;
    padding: 0;
    width: 1200px;
    height: 930px;
    overflow: hidden;
    background: var(--bg-light);
  }
  .postcard {
    position: relative;
    width: 1200px;
    height: 930px;
    overflow: hidden;
    font-family: "Delius", "Comic Sans MS", sans-serif;
    color: var(--ink);
  }
  .tools-backdrop {
    position: absolute;
    inset: 0;
    background:
      radial-gradient(ellipse at 75% 65%, rgba(170,120,90,0.45), transparent 60%),
      radial-gradient(ellipse at 40% 75%, rgba(185,150,125,0.35), transparent 55%),
      linear-gradient(100deg, var(--bg-light) 0%, var(--bg-mid) 55%, var(--bg-warm) 100%);
  }
  .brand-name {
    position: absolute;
    left: 38px;
    top: 30px;
    margin: 0;
    font-size: 76px;
    font-weight: 400;
    letter-spacing: 1px;
    color: var(--ink);
    white-space: nowrap;
  }
  .tagline {
    position: absolute;
    left: 52px;
    top: 140px;
    margin: 0;
    font-size: 30px;
    white-space: nowrap;
  }
  .contact {
    position: absolute;
    right: 50px;
    top: 60px;
    text-align: right;
    font-style: normal;
    white-space: nowrap;
  }
  .contact .address { font-size: 30px; line-height: 34px; }
  .contact .phone { font-size: 33px; margin-top: 30px; }
  .contact .email { font-size: 24px; margin-top: 34px; }
  .guarantees {
    position: absolute;
    left: 183px;
    width: 300px;
    top: 222px;
    text-align: center;
    color: var(--blue);
    font-size: 30px;
    line-height: 35px;
    margin: 0;
  }
  .starburst {
    position: absolute;
    left: 528px;
    top: 168px;
    width: 345px;
    height: 262px;
  }
  .starburst-text {
    position: absolute;
    left: 555px;
    top: 228px;
    width: 290px;
    text-align: center;
    color: var(--white);
    font-size: 25px;
    line-height: 34px;
    transform: rotate(-8deg);
    margin: 0;
  }
  .service-list {
    position: absolute;
    list-style: none;
    margin: 0;
    padding: 0;
    color: var(--blue);
    white-space: nowrap;
  }
  .service-list li::before { content: "- "; }
  .service-list--main {
    left: 46px;
    top: 322px;
    font-size: 28px;
    line-height: 36px;
  }
  .service-list--small {
    left: 300px;
    top: 400px;
    font-size: 26px;
    line-height: 36px;
  }
  .much-more {
    position: absolute;
    left: 306px;
    top: 815px;
    margin: 0;
    font-size: 30px;
    color: var(--ink);
  }
  .mascot {
    position: absolute;
    left: 865px;
    top: 355px;
    width: 305px;
    height: 545px;
    border-radius: 140px 140px 30px 30px;
    background: linear-gradient(180deg, var(--figure-a) 0%, var(--figure-b) 60%, #7b6a5c 100%);
    opacity: 0.85;
  }
</style>
</head>
<body>
<main class="postcard">
  <div class="tools-backdrop" role="img" aria-label="Faded photo of wrenches and hand tools behind the card"></div>

  <h1 class="brand-name">Miles ReadyFix</h1>
  <p class="tagline">25 years of experience. No job is too small.</p>

  <address class="contact">
    <div class="address">4172 Tamber Glen Rd NE,<br>Washington C.H. Ohio 43160</div>
    <div class="phone">740-318-2964</div>
    <div class="email">dkweller@mailbrook.net</div>
  </address>

  <p class="guarantees">One year warranty<br>Bonded and Insured<br>Cash or checks</p>

  <svg class="starburst" viewBox="0 0 380 280" preserveAspectRatio="none" aria-hidden="true">
    <polygon fill="var(--navy)" transform="translate(190 140) scale(1.1 0.82)"
      points="168,0 126,25 155,64 106,71 119,119 71,106 64,155 25,126 0,168 -25,126 -64,155 -71,106 -119,119 -106,71 -155,64 -126,25 -168,0 -126,-25 -155,-64 -106,-71 -119,-119 -71,-106 -64,-155 -25,-126 0,-168 25,-126 64,-155 71,-106 119,-119 106,-71 155,-64 126,-25"/>
  </svg>
  <p class="starburst-text">Handyman service.<br>Home repair.<br>Free estimates.</p>

  <ul class="service-list service-list--main">
    <li>Flooring</li>
    <li>Cabinets</li>
    <li>Decks</li>
    <li>Odd Jobs</li>
    <li>Carpentry</li>
    <li>Painting</li>
    <li>Drywall Repair</li>
    <li>Ceramic Tile</li>
    <li>Screen Repair</li>
    <li>Fence Repair</li>
    <li>Pressure Wash</li>
    <li>Hanging Pictures</li>
    <li>Wood Rot Repair</li>
    <li>Plumbing</li>
    <li>Electrical</li>
  </ul>

  <ul class="service-list service-list--small">
    <li>Install Ceiling Fan</li>
    <li>Replace Garbage Disposal</li>
    <li>Toilet Repair</li>
    <li>Install New Lighting</li>
    <li>Install Safety Grab Bars</li>
    <li>Caulk Tub or Kitchen</li>
    <li>Hang Blinds/Rods</li>
    <li>Replace a Switch/Outlet</li>
    <li>Replace/Adjust Doors and Locksets</li>
    <li>Replace Faucets/Sinks/Vanity Tops</li>
  </ul>

  <p class="much-more">And much more!</p>

  <div class="mascot" role="img" aria-label="Caricature of the handyman in a ranger drifton hat, glasses and full beard, holding a hammer and wearing a tool belt"></div>
</main>
</body>
</html>
```